依頼詳細
名刺デザインを新しくしたいと思っています。「シンプル」かつ「先進的」なデザインを希望します。名刺の背景は白地で、弊社イメージカラーのオレンジをメインカラーに使用していただきたいです。
関連性はありますが職種が違う二つの事業所のため、裏表をデザインは同じ(又は近似)でも指色を変える等の変化を付けつつ、統一性を持たせたものにしたいです。
記載項目
表面:クヌギリアルティ株式会社
代表取締役/住所/電話/FAX/Mobile/Mail/Web
資格名として、宅地建物取引士,賃貸不動産経営管理士,1級ファイナンシャル・プランイング技能士/CFP
事業内容:不動産売買・賃貸・運用 ※事業内容の文言は不要です
各種測量設計・構造計算等

裏面:クヌギリーガル行政書士|土地家屋調査士事務所
所長/住所/電話/FAX/Mobile/Mail/Web
資格名として、行政書士,土地家屋調査士
事業内容:各種許認可行政手続・相続遺言関係 ※事業内容の文言は不要です
不動産の表示に関する登記・境界に関する事項全般
希望イメージ
シンプル 複雑
単色 カラフル
暗い 明るい
日常 高級
遊び心 厳粛
未来的 伝統的
女性的 男性的
希望する色
黄・オレンジ系
納品ファイル
• イラストレーター形式 (.ai)
• PNG形式 (.png)
補足説明
会社ロゴは名刺に入れたいです。添付ファイルデータ3/4のロゴのみを使用してください。
新規事業部開設及び事務所移転が控えていますので、ご採用させていただいた方には今後看板デザインや封筒デザイン等の継続依頼も検討しております。

シンプルかつ洗練されたデザインが、イメージ通りでした。
特に柔らかい印象を与える雰囲気が秀逸でした。

この度は、数々のご提案をいただきまして誠にありがとうございました。
どのご提案も素晴らしいものばかりで、本当に選定には苦労いたしました。
私事ですが、今春から初夏にかけて新しい事業部の開設と会社の移転が控えております。
今後は封筒や看板デザイン、その他皆様のお力をお借りしたい案件がございますので、今後ともどうぞよろしくお願いいたします。
今般のご提案の数々につきまして、改めてお礼申し上げます。

```html
<!DOCTYPE html>
<html lang="ja">
<head>
<meta charset="utf-8">
<link rel="stylesheet" href="https://fonts.googleapis.com/css2?family=Noto+Sans+JP:wght@400;500;700&family=Noto+Serif+JP:wght@500;700&family=Noto+Serif:ital,wght@1,400&display=swap">
<style>
:root{
  --orange:#ef8a12;
  --orange-soft:#f6b15e;
  --ink:#333;
  --ink-light:#666;
  --rule:#555;
  --paper:#fff;
  --bg:#f1f1f1;
}
*{margin:0;padding:0;box-sizing:border-box}
html,body{width:841px;height:1200px;overflow:hidden;background:var(--bg)}
body{position:relative;font-family:"Noto Sans JP",sans-serif;color:var(--ink)}
.card{position:absolute;left:50px;width:740px;background:var(--paper);box-shadow:0 4px 14px rgba(0,0,0,.18);overflow:hidden}
.card--front{top:56px;height:470px}
.card--back{top:660px;height:460px}
.watermark{position:absolute;border-radius:50%;background:radial-gradient(circle,rgba(239,138,18,.10) 0%,rgba(239,138,18,.05) 60%,rgba(239,138,18,0) 75%)}
.front-mark{left:340px;top:150px;width:420px;height:420px}
.back-mark{left:330px;top:40px;width:440px;height:440px}
.divider-v{position:absolute;left:310px;top:14px;width:1px;height:440px;background:var(--rule)}
.rule{position:absolute;height:1px;background:var(--rule)}
.pointer{position:absolute;width:0;height:0}
.pointer--right{left:0;top:150px;border-top:18px solid transparent;border-bottom:18px solid transparent;border-left:22px solid var(--orange)}
.pointer--down{left:556px;top:0;border-left:16px solid transparent;border-right:16px solid transparent;border-top:22px solid var(--orange)}
.title{position:absolute;font-size:14px;color:var(--ink)}
.person{position:absolute;font-family:"Noto Serif JP",serif;font-weight:700;color:var(--orange);font-size:34px;letter-spacing:.15em}
.romaji{position:absolute;font-family:"Noto Serif",serif;font-style:italic;font-size:14px;color:var(--ink-light)}
.quals{position:absolute;font-size:12px;line-height:1.75;color:var(--ink)}
.brand{position:absolute;left:345px;top:62px;display:flex;align-items:center;gap:14px}
.brand-dot{width:40px;height:40px;border-radius:50%;background:var(--orange)}
.brand-name{font-size:26px;font-weight:500;color:var(--ink);letter-spacing:.04em}
.company{position:absolute;font-size:22px;font-weight:500;color:var(--ink);letter-spacing:.04em;line-height:1.5}
.contact{position:absolute;font-size:12.5px;color:var(--ink)}
.contact .row{display:flex;align-items:center;gap:18px;height:28px}
.item{display:flex;align-items:center;gap:7px}
.icon{width:18px;height:18px;flex:none}
.services{position:absolute;font-size:14px;line-height:1.9;color:var(--ink)}
.vertical{position:absolute;writing-mode:vertical-rl}
</style>
</head>
<body>

<section class="card card--front">
  <div class="watermark front-mark" role="img" aria-label="Faint company mark decoration"></div>
  <div class="divider-v"></div>

  <div class="pointer pointer--right"></div>
  <p class="title" style="left:56px;top:114px">代表取締役</p>
  <h1 class="person" style="left:56px;top:136px">椚田 直人</h1>
  <p class="romaji" style="left:58px;top:196px">Naoto Kunugida</p>
  <p class="quals" style="left:56px;top:246px">[宅地建物取引士]<br>[賃貸不動産経営管理士]<br>[1級ファイナンシャル]<br>[プランニング技能士/CFP]</p>

  <div class="brand"><span class="brand-dot"></span><span class="brand-name">KUNUGI REALTY</span></div>
  <h2 class="company" style="left:345px;top:128px">クヌギリアルティ株式会社</h2>

  <div class="contact" style="left:345px;top:170px">
    <div class="row"><span class="item"><svg class="icon" viewBox="0 0 18 18"><rect width="18" height="18" rx="3" fill="#ef8a12"/><path d="M9 3.5a4 4 0 0 1 4 4c0 3-4 7-4 7s-4-4-4-7a4 4 0 0 1 4-4z" fill="#fff"/></svg>〒700-0000　見本市本町1丁目2番地</span></div>
    <div class="row">
      <span class="item"><svg class="icon" viewBox="0 0 18 18"><rect width="18" height="18" rx="3" fill="#ef8a12"/><path d="M5 4h3l1 3-2 1a7 7 0 0 0 3 3l1-2 3 1v3c-6 0-9-3-9-9z" fill="#fff"/></svg>0000-11-2233</span>
      <span class="item"><svg class="icon" viewBox="0 0 18 18"><rect width="18" height="18" rx="3" fill="#ef8a12"/><rect x="4" y="6" width="10" height="7" fill="#fff"/><rect x="6" y="3.5" width="6" height="3" fill="#fff"/></svg>0000-11-4455</span>
    </div>
    <div class="row">
      <span class="item"><svg class="icon" viewBox="0 0 18 18"><rect width="18" height="18" rx="3" fill="#ef8a12"/><rect x="6" y="3" width="6" height="12" rx="1" fill="#fff"/></svg>090-0000-1234</span>
      <span class="item"><svg class="icon" viewBox="0 0 18 18"><rect width="18" height="18" rx="3" fill="#ef8a12"/><rect x="3.5" y="5" width="11" height="8" fill="#fff"/><path d="M3.5 5l5.5 4.5L14.5 5" stroke="#ef8a12" fill="none"/></svg>info@kunugi.example</span>
    </div>
    <div class="row"><span class="item"><svg class="icon" viewBox="0 0 18 18"><rect width="18" height="18" rx="3" fill="#ef8a12"/><circle cx="9" cy="9" r="5" fill="none" stroke="#fff" stroke-width="1.4"/><path d="M4 9h10M9 4v10" stroke="#fff" stroke-width="1.2"/></svg>http://www.kunugi-realty.example</span></div>
  </div>

  <div class="rule" style="left:310px;top:318px;width:410px"></div>
  <p class="services" style="left:345px;top:336px">・不動産売買・賃貸・運用<br>・各種測量設計・構造計算等</p>
</section>

<section class="card card--back">
  <div class="watermark back-mark" role="img" aria-label="Faint company mark decoration"></div>

  <h2 class="company" style="left:50px;top:110px;font-size:21px">クヌギリーガル行政書士<br>土地家屋調査士事務所</h2>

  <div class="contact" style="left:50px;top:196px">
    <div class="row"><span class="item"><svg class="icon" viewBox="0 0 18 18"><rect width="18" height="18" rx="3" fill="#ef8a12"/><path d="M9 3.5a4 4 0 0 1 4 4c0 3-4 7-4 7s-4-4-4-7a4 4 0 0 1 4-4z" fill="#fff"/></svg>〒700-0000　見本市本町1丁目2番地</span></div>
    <div class="row">
      <span class="item"><svg class="icon" viewBox="0 0 18 18"><rect width="18" height="18" rx="3" fill="#ef8a12"/><path d="M5 4h3l1 3-2 1a7 7 0 0 0 3 3l1-2 3 1v3c-6 0-9-3-9-9z" fill="#fff"/></svg>0000-11-2233</span>
      <span class="item"><svg class="icon" viewBox="0 0 18 18"><rect width="18" height="18" rx="3" fill="#ef8a12"/><rect x="4" y="6" width="10" height="7" fill="#fff"/><rect x="6" y="3.5" width="6" height="3" fill="#fff"/></svg>0000-11-4455</span>
    </div>
    <div class="row">
      <span class="item"><svg class="icon" viewBox="0 0 18 18"><rect width="18" height="18" rx="3" fill="#ef8a12"/><rect x="6" y="3" width="6" height="12" rx="1" fill="#fff"/></svg>090-0000-1234</span>
      <span class="item"><svg class="icon" viewBox="0 0 18 18"><rect width="18" height="18" rx="3" fill="#ef8a12"/><rect x="3.5" y="5" width="11" height="8" fill="#fff"/><path d="M3.5 5l5.5 4.5L14.5 5" stroke="#ef8a12" fill="none"/></svg>info@kunugi.example</span>
    </div>
    <div class="row"><span class="item"><svg class="icon" viewBox="0 0 18 18"><rect width="18" height="18" rx="3" fill="#ef8a12"/><circle cx="9" cy="9" r="5" fill="none" stroke="#fff" stroke-width="1.4"/><path d="M4 9h10M9 4v10" stroke="#fff" stroke-width="1.2"/></svg>http://www.kunugi-realty.example</span></div>
  </div>

  <div class="pointer pointer--down"></div>
  <p class="vertical title" style="left:640px;top:50px;letter-spacing:.2em">所長</p>
  <h1 class="vertical person" style="left:588px;top:48px">椚田 直人</h1>
  <p class="vertical romaji" style="left:560px;top:50px">Naoto Kunugida</p>
  <p class="quals" style="left:600px;top:250px;text-align:right;width:110px">[行政書士]<br>[土地家屋調査士]</p>

  <div class="rule" style="left:30px;top:310px;width:690px"></div>
  <p class="services" style="left:50px;top:326px">・各種許認可行政手続・相続遺言関係<br>・不動産の表示に関する登記・境界に関する事項全般</p>
</section>

</body>
</html>
```